A land page lead collector for people who want to reduce there postage costs

We are looking to create a single page website landing page to collect leads of people who want to reduce there postage costs.

The form should basically ask:

Name:
Business Name:
Address:
Town:
Post Code:
Email:
Phone:
Letter Volume Per Week:
Parcel Volume Per Week:

We should basically be advertising cheaper postage costs.

We will not be showing prices on this website we will just be collecting the leads.

Our competition website is as follows https://parcelwrenhub.com

But we are not a online service. This is just a collector to get leads of people who want to save money on there postage costs.
Updates

Target Market(s)

Small and medium sized enterprises

Industry/Entity Type

Advertising

Number of Pages Required

1 page

Colors
ec2027
0356a4

Requirements
Must have
• Form above the fold of the page
Nice to have
• Colour red and blue.
• Parallax design would be nice.

```html
<!DOCTYPE html>
<html lang="en">
<head>
<meta charset="utf-8">
<title>Quick Signup – Cheaper Postage</title>
<link href="https://fonts.googleapis.com/css2?family=Mulish:wght@300;400;600&display=swap" rel="stylesheet">
<style>
:root{
  --red:#ec2027;
  --red-panel:#ee3f4a;
  --blue:#0356a4;
  --blue-dark:#0a4e9b;
  --blue-soft:#7fa7d3;
  --white:#ffffff;
  --ink:#333a40;
  --heading-blue:#1361ad;
  --page:#f4f4f6;
}
*{box-sizing:border-box;margin:0;padding:0}
html,body{width:962px;height:1200px;overflow:hidden}
body{font-family:"Mulish",sans-serif;background:var(--page);position:relative;color:var(--ink)}
.hero{position:absolute;left:0;top:0;width:962px;height:603px;overflow:hidden}
.hero-photo{position:absolute;inset:0;background:
  radial-gradient(ellipse at 60% 30%,#3a2f31 0%,rgba(58,47,49,0) 35%),
  radial-gradient(ellipse at 70% 80%,#d9d9df 0%,rgba(217,217,223,0) 30%),
  linear-gradient(90deg,#8a6f6a 0%,#b7a49c 35%,#8d8480 60%,#c9c3c0 85%,#a29e9d 100%)}
.signup{position:absolute;left:78px;top:0;width:298px;height:603px;background:var(--red-panel);text-align:center;color:var(--white)}
.edge{position:absolute;top:0;width:5px;height:603px}
.edge-left{left:-4px}.edge-right{right:-4px}
.ribbon{position:absolute;left:0;top:0;width:60px;height:78px;background:var(--blue);color:#c8d7ea;font-size:10px;line-height:1;padding-top:12px;clip-path:polygon(0 0,100% 0,100% 100%,50% 90%,0 100%)}
.ribbon b{display:block;color:var(--white);font-size:18px;font-weight:600;margin:4px 0 3px}
.stamps{position:absolute;left:78px;top:68px;width:136px;height:82px;border-radius:3px;background:linear-gradient(90deg,#f1a23e 0%,#e8734a 45%,#c9d5e4 55%,#6f9cc8 100%)}
.title{position:absolute;left:0;right:0;top:168px;font-weight:300;font-size:18px;line-height:1}
.subtitle{position:absolute;left:0;right:0;top:188px;font-size:10px}
.form{position:absolute;left:38px;top:214px;width:218px}
.field{height:28px;background:var(--white);border-bottom:2px solid #c4151c;margin-bottom:2px;font-size:9.5px;color:#333;text-align:left;padding:9px 9px 0;position:relative}
.field.gap{margin-top:3px}
.select::after{content:"";position:absolute;right:0;top:0;width:24px;height:28px;background:var(--blue-soft)}
.select svg{position:absolute;right:8px;top:11px;z-index:1}
.submit{margin-top:17px;height:28px;background:var(--blue-dark);font-size:10px;line-height:28px;color:var(--white);text-align:center}
.hero-copy{position:absolute;left:465px;top:245px;color:var(--white);font-weight:300;font-size:31px;line-height:42px}
.cta{position:absolute;left:466px;top:384px;width:218px;height:28px;background:var(--blue);color:var(--white);font-size:10px;line-height:28px;text-align:center}
.social{position:absolute;right:44px;top:28px;display:flex;gap:6px}
.social span{display:flex;align-items:center;gap:3px;font-size:8px;color:var(--white)}
.social i{width:10px;height:10px;border:1px solid var(--white);border-radius:50%}
.offers{position:absolute;left:0;top:603px;width:962px;height:519px;background:
  radial-gradient(ellipse at 80% 20%,rgba(236,140,120,.22),rgba(236,140,120,0) 45%),
  radial-gradient(ellipse at 40% 10%,rgba(120,170,150,.18),rgba(120,170,150,0) 40%),
  linear-gradient(90deg,#f7f7f8 0%,#eceef1 60%,#e9e5e6 100%)}
.offers h2{position:absolute;left:77px;top:178px;font-weight:400;font-size:27px;line-height:33px;color:var(--heading-blue)}
.offers ul{position:absolute;left:78px;top:258px;list-style:none;font-size:17px;color:var(--ink)}
.offers li{height:30px;display:flex;align-items:baseline}
.offers li::before{content:"";width:6px;height:6px;border-radius:50%;background:#222;margin-right:9px;align-self:center}
.offers sup{font-size:14px;margin:0 3px}
.video{position:absolute;left:471px;top:137px;width:412px;height:294px;background:radial-gradient(ellipse at 60% 40%,#3b3f45 0%,#16181b 70%)}
.video svg{position:absolute;left:184px;top:125px}
.footer{position:absolute;left:0;top:1122px;width:962px;height:78px;background:var(--blue-dark);color:var(--white);font-size:12px;text-align:center;line-height:78px}
</style>
</head>
<body>
<section class="hero">
  <div class="hero-photo" role="img" aria-label="Photo of a smiling woman unpacking a parcel filled with bubble wrap in a bright room with bookshelves"></div>
  <nav class="social" aria-label="Social links">
    <span><i></i>Friendly</span><span><i></i>Linkwork</span><span><i></i>Chirpline</span>
  </nav>
  <h1 class="hero-copy">Lorem ipsum dolor<br>sit amet, consectetur<br>adipisicing</h1>
  <div class="cta">Click to Get in Touch</div>

  <aside class="signup">
    <svg class="edge edge-left" viewBox="0 0 5 603" preserveAspectRatio="none"><defs><pattern id="zz" width="5" height="6" patternUnits="userSpaceOnUse"><polygon points="5,0 0,3 5,6" fill="#ee3f4a"/></pattern></defs><rect width="5" height="603" fill="url(#zz)"/></svg>
    <svg class="edge edge-right" viewBox="0 0 5 603" preserveAspectRatio="none"><defs><pattern id="zz2" width="5" height="6" patternUnits="userSpaceOnUse"><polygon points="0,0 5,3 0,6" fill="#ee3f4a"/></pattern></defs><rect width="5" height="603" fill="url(#zz2)"/></svg>
    <div class="ribbon">100%<b>FREE</b>Soon</div>
    <div class="stamps" role="img" aria-label="Illustration of two postage stamps showing city buildings"></div>
    <h2 class="title">Quick Signup</h2>
    <p class="subtitle">lorem ipsum dolor sit amet</p>
    <form class="form">
      <div class="field">Name</div>
      <div class="field">Business Name</div>
      <div class="field">Address</div>
      <div class="field">Post Code</div>
      <div class="field select gap">Town<svg width="8" height="6" viewBox="0 0 8 6"><path d="M1 1l3 3 3-3" stroke="#fff" stroke-width="1.5" fill="none"/></svg></div>
      <div class="field gap">Phone</div>
      <div class="field">Email</div>
      <div class="field select gap">Letter Volume Per Week<svg width="8" height="6" viewBox="0 0 8 6"><path d="M1 1l3 3 3-3" stroke="#fff" stroke-width="1.5" fill="none"/></svg></div>
      <div class="field select">Parcel Volume Per Week<svg width="8" height="6" viewBox="0 0 8 6"><path d="M1 1l3 3 3-3" stroke="#fff" stroke-width="1.5" fill="none"/></svg></div>
      <div class="submit">Submit Now</div>
    </form>
  </aside>
</section>

<section class="offers" role="img" aria-label="Faint background of scattered postage stamps">
  <h2>Lorem ipsum dolor sit amet<br>consectetur adipisicing</h2>
  <ul>
    <li>34%<sup>off</sup>National Postage</li>
    <li>25%<sup>off</sup>International Postage</li>
    <li>Free upto 100gm - Parcel, Packet</li>
  </ul>
  <div class="video" role="img" aria-label="Video still of hands typing on a laptop showing dashboard charts">
    <svg width="34" height="42" viewBox="0 0 34 42"><polygon points="0,0 34,21 0,42" fill="#fff"/></svg>
  </div>
</section>

<footer class="footer">Copyright © 2015</footer>
</body>
</html>
```